Website - TSCR

Having reviewed the designs received so far, no one design is meeting the client’s needs. The client has identified desirable elements from the designs submitted, which we want to see brought together.
Header
It is important that the logo is given space – ie is not overlayed on an image, nor with a short fade into an image. A gradual fade into the header image is acceptable.
Background
While an image background is acceptable, this should only be visible on the left and right borders, it should not be used underneath the main content area.
Main menu
The main menu should be a cohesive bar across the page – not separate buttons. Buttons that are connected together within a bar are acceptable. Menu items should be separated using a pipe ( | ), or by being framed (as long as the framing sits within a bar). Menu item should change colour to indicate the page you are on.
Left Hand Boxes
There should be consistency in colouring through these. It is acceptable to use one colour for the heading , and another for the content area. It is not acceptable for each box to have a different scheme. This applies to the right hand feature boxes as well.
Colouring
We want to keep this simple. Please use colours from the logo, feel free to add complimentary colours but keep the palette limited. If shading is used with any of the colours be careful to not move it too far from the original colour. The yellow does not look good with too much of a grey shade.
Feature Boxes
The two feature boxes on the home page (Browse Homes and Local Knowledge) need to stand out. An option is to ensure that the associated link button uses one of the brighter colours in the palette.
_____________________________________________________
Note: I have attached the newly design logo to the brief. It is important that colours from the logo are used on the design. Blue denotes water and the yellow denotes sand and sun.
I'd like to see the feel of the logo reflected in the site.
______________________________________________
Tui Shore and Coastal Retreats is rebuilding its website – www.tuishoreandcoastalretreats.co.nz.
We require the design of two pages:
• Home
• House detail page (pgs 3-5 of the attachment).
We have specified a layout for the site (attached).
The contextual information below provides the feeling the site needs to convey.
If further information is required please contact us.
CONTEXT/BACKGROUND
Tui Shore and Coastal Retreats (TSCR) has been in business now for over 11 years and is due for a facelift. We have about 40 – 60 houses available during the peak summer period – about 50% are permanent holiday homes, the balance are local family homes being rented out while they are away on holiday.
We are currently located in Ohope Beach – but with the national name have the ability and goal to expand into other areas of New Zealand – so any logo etc has to have the ability to represent other holiday destinations within NZ. Bear in mind that our primary location is Ohope at the moment.
Our key market is families going on holiday – looking for a holiday home to book (currently an Ohope Beach holiday)
Secondary market is couples or mature groups looking at having some R&R or business groups having some team building/ management meetings away from the busy office surroundings.
We manage ALL the properties so are a great source of information on what holiday home is best suited to each family and “things to do” in the area – i.e. other activities.
Our main focus is to be the best “holiday home” - accommodation provider in whatever location TSCR is representing. We want to be seen as having a good supply of great homes, providing a great service as well as being a good source of local knowledge.
We want to be seen as PROFESSIONALS in the holiday rental business (from occupants and owners).
TRUST – we want people to be able to trust us by listing their property with us (owners) and confidently booking accommodation through us (occupants).
TAGLINE SUGGESTIONS
Key motif – “TSCR, your door to a fine escape!” The “key”, of course is a double play on the house key you get. But it is also extendible to other aspect of the experience we offer. For example the phrase: “getting the key to the city” is applicable to us – we give them the key to Ohope…(or whatever location we are marketing in the future). Potentially we may consider promotional merchandise around this, eg promo key rings etc.
Some key words/phrases that our business represents are:
• ‘Our place is your place’
• Connect – connecting families to holiday homes and the area – at the moment only Ohope.
• Local – local people looking after your needs – “our place is your place – so make yourself at home!”
• Link – we are the link to a real kiwi holiday experience.
• Holiday - R&R – rest and recreation
More specific to Ohope:
• Safe Natural playground – beach, bush, fishing, outdoor activities – creating real family memories.
Website:
• Need to focus on the Local and Personal property management factors in website to differentiate us from other nationwide listing sites – contact us and we can help you find the right accommodation and save you time
• Play on the HOLIDAYMAKER experience more, including giving prominence to visitor deals, become a local etc, differentiating us from other local holiday home rental businesses.
• Real – real people, real places, real experiences.
• User friendly, informative, professional with a personal touch/feel, to encourage the holiday feeling.
Reason: We had put this project on hold pending the design of a new logo.
Having reviewed the designs received so far, no one design is meetingthe client’s needs. The client has identified desirable elements from thedesigns submitted, which we want to see brought together.
Header
It is important that the logo is given space – ie is not overlayed on animage, nor with a short fade into an image. A gradual fade into the headerimage is acceptable.
Background
While an image background is acceptable, this should only be visible onthe left and right borders, it should not be used underneath the main contentarea.
Main menu
The main menu should be a cohesive bar across the page – not separatebuttons. Buttons that are connected together within a bar are acceptable.Menu items should be separated using a pipe ( | ), or by being framed (as longas the framing sits within a bar). Menu item should change colour to indicatethe page you are on.
Left Hand Boxes
There should be consistency in colouring through these. It isacceptable to use one colour for the heading , and another for the contentarea. It is not acceptable for each box to have a different scheme. Thisapplies to the right hand feature boxes as well.
Colouring
We want to keep this simple. Please use colours from the logo,feel free to add complimentary colours but keep the palette limited. Ifshading is used with any of the colours be careful to not move it too far fromthe original colour. The yellow does not look good with too much of agrey shade.
Feature Boxes
The two feature boxes on the home page (Browse Homes and LocalKnowledge) need to stand out. An option is to ensure that the associated linkbutton uses one of the brighter colours in the palette.

```html
<!DOCTYPE html>
<html lang="en">
<head>
<meta charset="utf-8">
<title>Tui Shore and Coastal Retreats – Home</title>
<link rel="stylesheet" href="https://fonts.googleapis.com/css2?family=Arimo:ital,wght@0,400;0,700;1,700&family=Ubuntu:wght@300;400;500&display=swap">
<style>
:root{
  --cream:#fdf2da;
  --sand:#e6d3b0;
  --sand-dark:#cdb78f;
  --yellow:#fcd23a;
  --yellow-deep:#f7b51e;
  --orange:#f39a1c;
  --blue:#1aa3e8;
  --blue-deep:#0b78c8;
  --blue-light:#5ec3f3;
  --ink:#1b1b1b;
  --link:#0a66c9;
  --footer:#111;
  --white:#fff;
}
*{box-sizing:border-box;margin:0;padding:0}
html,body{width:901px;height:1200px;overflow:hidden}
body{background:var(--cream);font-family:Arimo,Arial,sans-serif;color:var(--ink);position:relative}
.abs{position:absolute}

.sand-band{left:0;top:262px;width:901px;height:90px;background:linear-gradient(180deg,var(--sand) 0%,var(--sand-dark) 50%,var(--cream) 100%)}

.brand{left:47px;top:60px;width:220px;display:flex;align-items:center;gap:10px;font-family:Ubuntu,sans-serif;font-size:22px;line-height:1.15;color:var(--blue-deep);font-weight:500}
.brand-dot{width:34px;height:34px;border-radius:50%;background:var(--yellow-deep);flex:none}

.hero{left:315px;top:20px;width:573px;height:221px;border-radius:10px;overflow:hidden;border:1px solid #666}
.hero-photo{width:100%;height:100%;background:linear-gradient(160deg,#9fd0ef 0%,#e9eef0 40%,#b9a58d 70%,#5b86a0 100%)}
.hero-caption{left:0;bottom:0;width:100%;height:46px;background:linear-gradient(180deg,rgba(30,30,30,.75),rgba(10,10,10,.9));display:flex;align-items:center;justify-content:space-between;padding:0 14px 0 70px}
.hero-caption p{font-family:Ubuntu,sans-serif;color:var(--white);font-size:24px}
.dots{display:flex;gap:5px}
.dots span{width:13px;height:13px;border-radius:50%;border:2px solid var(--white);background:var(--blue)}
.dots span:first-child{background:transparent}

.menu{left:9px;top:279px;width:883px;height:43px;border-radius:22px;background:linear-gradient(180deg,#fff2a8 0%,var(--yellow) 35%,var(--yellow-deep) 100%);border:1px solid #e7a312;display:flex;align-items:center;justify-content:center;font-size:15px}
.menu a{color:#2a1d00;text-decoration:none;padding:0 18px}
.menu a.current{color:var(--blue-deep)}
.menu .pipe{color:#2a1d00}

.box{left:9px;width:243px;border-radius:9px;overflow:hidden}
.box h2{font-family:Ubuntu,sans-serif;font-weight:400;font-size:22px;color:var(--white);padding:10px 14px 6px}
.search{top:338px;height:252px;background:linear-gradient(180deg,var(--yellow) 0%,var(--yellow-deep) 55%,var(--orange) 100%)}
.search label{display:block;font-size:12px;font-weight:700;color:#2a1d00;margin:8px 0 3px 17px}
.field{height:15px;background:var(--white);border:1px solid #b9b9b9;font-size:9px;color:#999;padding:1px 3px;position:relative}
.field.select::after{content:"";position:absolute;right:5px;top:5px;border:4px solid transparent;border-top-color:#222}
.row{display:flex;align-items:center;margin-left:17px}
.row .to{font-size:13px;font-weight:700;margin:0 12px}
.search-actions{display:flex;align-items:center;gap:14px;margin:14px 0 0 17px}
.pill{display:inline-flex;align-items:center;gap:6px;border-radius:8px;font-size:13px;padding:2px 10px}
.pill-blue{background:linear-gradient(180deg,var(--blue-light),var(--blue-deep));color:var(--white)}
.pill-yellow{background:linear-gradient(180deg,#fff1a0,var(--yellow-deep));color:#2a1d00;border:1px solid #c98a10}
.more{font-size:12px;color:#2a1d00;text-decoration:underline}

.touch{top:600px;height:269px;background:linear-gradient(180deg,var(--blue-light) 0%,var(--blue) 40%,var(--blue-deep) 100%)}
.touch .intro{font-size:10.5px;color:#0b1e33;margin:4px 18px 10px;line-height:1.25;font-weight:700}
.touch .line{display:flex;align-items:center;margin:0 0 10px 17px;font-size:13px;color:var(--white)}
.touch .line .field{width:167px;margin-left:auto;margin-right:14px;height:16px}
.touch .submit{text-align:right;margin:4px 14px 0}
.find{position:absolute;left:0;top:196px;width:100%;height:73px;border-top:1px solid rgba(255,255,255,.35);display:flex;align-items:center;padding-left:16px;gap:10px}
.find p{font-family:Ubuntu,sans-serif;color:var(--white);font-size:20px;line-height:.95;width:70px}
.net{width:66px;height:50px;display:flex;align-items:center;justify-content:center;font-size:12px;color:var(--white);font-weight:700}

.deal{top:878px;height:185px;background:linear-gradient(180deg,var(--yellow) 0%,var(--yellow-deep) 60%,var(--orange) 100%)}
.deal-body{display:flex;gap:6px;margin:4px 10px 0 15px}
.deal-photo{width:74px;height:82px;flex:none;background:linear-gradient(135deg,#c8924e,#6b3b1c)}
.deal-body p{font-size:9px;color:var(--white);line-height:1.35}
.deal-foot{display:flex;justify-content:space-between;align-items:center;margin:12px 14px 0 22px}
.price{color:var(--white);font-weight:700;font-style:italic;font-size:14px}

.like{left:9px;top:1072px;width:46px;height:20px;border:1px solid #9aa6c0;background:#eef1f7;border-radius:3px;font-size:11px;color:#3b5a99;display:flex;align-items:center;justify-content:center}
.share{left:9px;top:1096px;display:flex;align-items:center;gap:8px;font-size:12px;color:var(--ink)}
.share .chip{height:24px;padding:0 5px;border-radius:3px;display:flex;align-items:center;font-size:10px;font-weight:700;color:var(--white);background:var(--blue-deep)}

.welcome{left:267px;top:344px;width:440px;font-family:Ubuntu,sans-serif;font-weight:400;font-size:20px;color:#222;border-bottom:1px solid #bbb;padding-bottom:4px}
.welcome small{font-size:15px}
.copy{font-size:10.7px;line-height:16.6px;color:var(--ink)}

.help{left:724px;top:340px;width:168px;height:196px;border-radius:8px;background:linear-gradient(180deg,var(--blue-light),var(--blue));border:1px solid #3b9bd8}
.help-tab{position:absolute;left:-4px;top:16px;width:118px;height:36px;background:linear-gradient(180deg,var(--yellow),var(--orange));font-family:Ubuntu,sans-serif;color:var(--white);font-size:22px;display:flex;align-items:center;padding-left:20px;gap:22px;border-radius:3px 0 0 3px}
.help-tab::after{content:"";position:absolute;right:-14px;top:0;border-left:14px solid var(--orange);border-top:18px solid transparent;border-bottom:18px solid transparent}
.help h3{position:absolute;left:6px;top:62px;font-size:11px;font-style:italic;font-weight:700;color:#0b1e33;line-height:1.2}
.help p{position:absolute;left:14px;top:98px;font-size:10.5px;color:#0b1e33;line-height:1.3}
.help .call{position:absolute;left:9px;top:130px;font-size:16px;font-style:italic;font-weight:700;color:var(--white);line-height:1.25}

.prompt{left:267px;top:764px;width:625px;font-size:16px;font-weight:700;font-style:italic;line-height:19px;text-transform:uppercase;letter-spacing:.3px}
.prompt a{color:var(--link)}

.feature{top:809px;width:310px;height:177px;border-radius:8px;border:1px solid #d3c8b0}
.feature-a{left:260px;background:linear-gradient(135deg,#3d4a6a 0%,#c9c7cc 45%,#1f3f7a 100%)}
.feature-b{left:582px;background:linear-gradient(160deg,#7ec6ee 0%,#bfe4f2 40%,#2f8a3d 70%,#e9d9a6 100%)}
.feature-btn{top:968px;width:247px;height:46px;border-radius:8px;background:linear-gradient(180deg,var(--yellow) 0%,var(--orange) 100%);border:1px solid #d98010;display:flex;align-items:center;justify-content:center;font-family:Ubuntu,sans-serif;font-size:21px;color:#222;text-transform:uppercase;text-decoration:none}

.footer{left:9px;top:1144px;width:883px;height:43px;border-radius:12px;background:linear-gradient(180deg,#555 0%,var(--footer) 45%,#000 100%);color:var(--white);font-size:10px;text-align:center;padding-top:7px;line-height:16px}
.footer .sep{margin:0 8px}
</style>
</head>
<body>

<div class="abs sand-band"></div>

<div class="abs brand"><span class="brand-dot"></span><span>Tui Shore &amp; Coastal Retreats</span></div>

<div class="abs hero">
  <div class="hero-photo" role="img" aria-label="Photo of a modern beachfront holiday home with a pool and terrace"></div>
  <div class="abs hero-caption">
    <p>TSCR, your door to a fine escape!</p>
    <div class="dots"><span></span><span></span><span></span><span></span><span></span></div>
  </div>
</div>

<nav class="abs menu">
  <a class="current" href="#">Home</a><span class="pipe">|</span>
  <a href="#">Browse Homes</a><span class="pipe">|</span>
  <a href="#">Packages</a><span class="pipe">|</span>
  <a href="#">Local Knoweldges</a><span class="pipe">|</span>
  <a href="#">About Us</a><span class="pipe">|</span>
  <a href="#">Contact Us</a><span class="pipe">|</span>
  <a href="#">List Your Home</a>
</nav>

<section class="abs box search">
  <h2>Quick Search</h2>
  <label>No. of Guest</label>
  <div class="row"><div class="field select" style="width:212px">Feb 2011</div></div>
  <label>Nightly Rate</label>
  <div class="row"><div class="field select" style="width:86px">Feb 2011</div><span class="to">TO</span><div class="field select" style="width:86px">$200</div></div>
  <label>Keywords</label>
  <div class="row"><div class="field" style="width:212px">Beach access</div></div>
  <div class="search-actions"><span class="pill pill-blue">enter &raquo;</span><a class="more" href="#">Advanced Search</a></div>
</section>

<section class="abs box touch">
  <h2>Keep in Touch</h2>
  <p class="intro">Newsletter with Deals &amp; Local Knowledge To Your Inbox</p>
  <div class="line">Name<div class="field"></div></div>
  <div class="line">Email<div class="field"></div></div>
  <div class="submit"><span class="pill pill-yellow">submit &raquo;</span></div>
  <div class="find">
    <p>Find us On</p>
    <span class="net">Pallora</span>
    <span class="net">Chirpwell</span>
  </div>
</section>

<section class="abs box deal">
  <h2>Deal</h2>
  <div class="deal-body">
    <div class="deal-photo" role="img" aria-label="Photo of a warmly lit holiday home bedroom"></div>
    <p>Lorem ipsum onsectetuer adipiscing elit, sed diam nonummy nibh euismod tincidunt ut laoreet lore magna aliquam erat volutpat. Ut wisi enim ad minim veniam, quis</p>
  </div>
  <div class="deal-foot"><span class="price">$1955.55</span><span class="pill pill-yellow">view &raquo;</span></div>
</section>

<div class="abs like">Like</div>
<div class="abs share">
  <span>Share This</span>
  <svg width="26" height="20" viewBox="0 0 26 20" aria-label="Email"><rect x="1" y="2" width="24" height="16" fill="#e8eef5" stroke="#7a8aa0"/><path d="M1 2l12 9 12-9" fill="none" stroke="#7a8aa0"/></svg>
  <span class="chip">Pallora</span>
  <span class="chip" style="background:var(--blue)">Chirpwell</span>
  <svg width="24" height="24" viewBox="0 0 24 24" aria-label="Share"><rect width="24" height="24" rx="3" fill="#3e9a2c"/><circle cx="7" cy="12" r="3" fill="#fff"/><circle cx="17" cy="6" r="3" fill="#fff"/><circle cx="17" cy="18" r="3" fill="#fff"/><path d="M7 12L17 6M7 12l10 6" stroke="#fff" stroke-width="1.6"/></svg>
</div>

<h1 class="abs welcome"><small>Welcome to</small> Tui Shore &amp; Coastal Retreats</h1>

<p class="abs copy" style="left:267px;top:383px;width:440px">Lorem ipsum onsectetuer adipiscing elit, sed diam nonummy nibh euismod tincidunt ut laoreet dolore magna aliquam erat volutpat. Ut wisi enim ad minim veniam, quis nostrud exerci tation ullamcorper suscipit lobortis nisl ut aliquip ex ea commodo consequat.</p>
<p class="abs copy" style="left:267px;top:450px;width:440px">Lorem ipsum onsectetuer adipiscing elit, sed diam nonummy nibh euismod tincidunt ut laoreet dolore magna aliquam erat volutpat. Ut wisi enim ad minim veniam, quis nostrud exerci tation ullamcorper suscipit lobortis nisl ut aliquip ex ea commodo consequat.Lorem ipsum onsectetuer adipiscing elit, sed diam nonummy nibh euismod tincidunt ut laoreet dolore magna aliquam erat volutpat. Ut wisi enim ad minim veniam, quis nostrud exerci tation ullamcorper suscipit lobortis nisl ut aliquip ex ea commodo</p>
<p class="abs copy" style="left:269px;top:560px;width:620px">Lorem ipsum onsectetuer adipiscing elit, sed diam nonummy nibh euismod tincidunt ut laoreet dolore magna aliquam erat volutpat. Ut wisi enim ad minim veniam, quis nostrud exerci tation ullamcorper suscipit lobortis nisl ut aliquip ex ea commodo consequat.</p>
<p class="abs copy" style="left:269px;top:625px;width:620px">Lorem ipsum onsectetuer adipiscing elit, sed diam nonummy nibh euismod tincidunt ut laoreet dolore magna aliquam erat volutpat. Ut wisi enim ad minim veniam, quis nostrud exerci tation ullamcorper suscipit lobortis nisl ut aliquip ex ea commodo consequat.Lorem ipsum onsectetuer adipiscing elit, sed diam nonummy nibh euismod tincidunt ut laoreet dolore magna aliquam erat volutpat. Ut wisi enim ad minim veniam, quis nostrud exerci tation ullamcorper suscipit lobortis nisl ut aliquip ex ea commodo consequat.</p>

<aside class="abs help">
  <div class="help-tab">Help
    <svg width="14" height="14" viewBox="0 0 14 14" aria-hidden="true"><path d="M6 2H2v10h10V8" fill="none" stroke="#fff" stroke-width="1.5"/><path d="M8 1h5v5M13 1L6 8" fill="none" stroke="#fff" stroke-width="1.5"/></svg>
  </div>
  <h3>CAN’T FIND WHAT YOU’RE LOOKING FOR?</h3>
  <p>Contact Us For A Personal<br>Property Search</p>
  <p class="call">&nbsp;Call Us At<br>+64-21-555-0142</p>
</aside>

<p class="abs prompt">Just can’t find what you’re looking for? <a href="#">Contact Us</a> for a personal property search.</p>

<div class="abs feature feature-a" role="img" aria-label="Photo of a holiday home dining room with sea view at dusk"></div>
<div class="abs feature feature-b" role="img" aria-label="Photo of a catamaran on a palm-lined sandy beach"></div>
<a class="abs feature-btn" style="left:291px" href="#">Browse Homes</a>
<a class="abs feature-btn" style="left:614px" href="#">Local Knowledge</a>

<footer class="abs footer">
  Terms &amp; Conditions<span class="sep">|</span>Privacy Policy<span class="sep">|</span>Contact Us<span class="sep">|</span>List Your Home<br>
  &copy; 2011, All Rights Reserved,
</footer>

</body>
</html>
```